Halvorsen & Tate Client Brochure

I need a Tri- fold brochure for a Custom cabinet company who has first rate skilled millworkers who custom craft cabinets from kitchens, bathrooms, living room entertainment centers, bedrooms to beautiful custom library's, fireplace mantels as well as garages and basement storage units and shelves. They also have a large selection of in stock mouldings. The company has been in business since 1943.See New logo, photos along with old business card and lets create brochure that's fresh and exciting.

Target Market(s)

Homeowners

Industry/Entity Type

It Company

Requirements
Must have
• Company Logo, Business Address, clear photos etc
Nice to have
• Clean and professional looking brochure.

```html
<!DOCTYPE html>
<html lang="en">
<head>
<meta charset="utf-8">
<title>Halvorsen &amp; Tate – Tri-fold Brochure</title>
<link href="https://fonts.googleapis.com/css2?family=Oswald:wght@400;500&family=Lato:wght@400;700&display=swap" rel="stylesheet">
<style>
  :root {
    --gold: #e0a526;
    --charcoal: #3d3d3d;
    --charcoal-dark: #2b2b2b;
    --paper: #ffffff;
    --mist: #eeeeee;
    --ink: #1e1e1e;
    --backdrop: #dcdcdc;
  }
  * { box-sizing: border-box; margin: 0; padding: 0; }
  html, body { width: 1200px; height: 1200px; overflow: hidden; background: var(--backdrop); }
  .canvas { position: relative; width: 1200px; height: 1200px; }
  .brochure {
    position: absolute; left: 40px; top: 167px; width: 1120px; height: 866px;
    background: var(--paper); box-shadow: 0 6px 24px rgba(0,0,0,.18);
  }
  .brochure-art { position: absolute; inset: 0; }
  .text { position: absolute; font-family: "Lato", sans-serif; }

  .service-list { left: 58px; top: 262px; width: 270px; color: var(--paper); }
  .service-list h3 {
    font-family: "Oswald", sans-serif; font-weight: 500; font-size: 15px;
    color: var(--gold); text-transform: uppercase; margin-bottom: 4px;
  }
  .service-list ul { list-style: none; font-size: 14.5px; line-height: 20px; margin-bottom: 18px; }
  .service-list li::before {
    content: ""; display: inline-block; width: 6px; height: 6px; border-radius: 50%;
    background: var(--gold); margin-right: 7px; vertical-align: middle;
  }
  .website { left: 0; width: 373px; top: 640px; text-align: center; font-size: 14px; letter-spacing: 1px; color: var(--ink); }

  .showroom { left: 373px; width: 373px; top: 508px; text-align: center; color: var(--ink); }
  .showroom h2 {
    font-family: "Oswald", sans-serif; font-weight: 500; font-size: 21px; color: var(--gold);
    text-transform: uppercase; display: inline-block; border-bottom: 2px solid var(--gold);
    line-height: 1.15; margin-bottom: 22px;
  }
  .showroom p { font-size: 13.5px; line-height: 18px; margin-bottom: 18px; }

  .brand { left: 746px; width: 374px; top: 58px; text-align: center; color: var(--gold); }
  .brand-name { font-family: "Lato", sans-serif; font-weight: 700; font-size: 26px; letter-spacing: 1px; text-transform: uppercase; }
  .brand-since { font-size: 12px; letter-spacing: 4px; margin-top: 6px; display: flex; align-items: center; justify-content: center; gap: 8px; }
  .brand-since::before, .brand-since::after { content: ""; width: 60px; height: 1px; background: var(--gold); }
  .brand-tag { font-size: 11px; letter-spacing: 1.5px; margin-top: 4px; text-transform: uppercase; }

  .headline {
    left: 746px; width: 374px; top: 560px; text-align: center;
    font-family: "Oswald", sans-serif; font-weight: 500; font-size: 28px; line-height: 34px;
    text-transform: uppercase; color: var(--ink);
  }
  .headline .accent { color: var(--gold); }
</style>
</head>
<body>
<main class="canvas">
  <article class="brochure">
    <svg class="brochure-art" width="1120" height="866" viewBox="0 0 1120 866">
      <defs>
        <linearGradient id="livingRoomTone" x1="0" y1="0" x2="1" y2="1">
          <stop offset="0" stop-color="#5b5853"/>
          <stop offset=".45" stop-color="#d8d1c4"/>
          <stop offset="1" stop-color="#6e6a64"/>
        </linearGradient>
        <linearGradient id="kitchenTone" x1="0" y1="0" x2="1" y2="1">
          <stop offset="0" stop-color="#e9e4da"/>
          <stop offset=".6" stop-color="#a67a4a"/>
          <stop offset="1" stop-color="#7a4a22"/>
        </linearGradient>
        <linearGradient id="showroomWash" x1="0" y1="0" x2="0" y2="1">
          <stop offset="0" stop-color="#f4f4f4"/>
          <stop offset="1" stop-color="#e2e2e2"/>
        </linearGradient>
        <linearGradient id="mouldingTone" x1="0" y1="0" x2="1" y2="1">
          <stop offset="0" stop-color="#f1e6d3"/>
          <stop offset="1" stop-color="#b88c5c"/>
        </linearGradient>
        <linearGradient id="rackTone" x1="0" y1="0" x2="1" y2="1">
          <stop offset="0" stop-color="#c9a47a"/>
          <stop offset="1" stop-color="#8a5f36"/>
        </linearGradient>
      </defs>

      <!-- inside left and centre panels: living room image -->
      <rect class="photo-living" role="img" aria-label="Bright living room with grey sectional sofa, curtains and city view windows" x="0" y="0" width="746" height="300" fill="url(#livingRoomTone)"/>

      <!-- centre panel body -->
      <path d="M373,282 C480,262 620,268 746,250 L746,866 L373,866 Z" fill="url(#showroomWash)"/>
      <path d="M373,276 C480,256 620,262 746,244 L746,256 C620,274 480,268 373,288 Z" fill="var(--charcoal)"/>

      <!-- left panel swoosh and service box -->
      <path d="M0,82 C120,182 250,232 373,250 L373,866 L0,866 Z" fill="var(--paper)"/>
      <path d="M0,64 C120,166 250,220 373,236 L373,254 C240,240 120,196 0,120 Z" fill="var(--gold)"/>
      <path d="M32,138 C140,206 250,236 340,246 L340,548 Q340,580 308,580 L64,580 Q32,580 32,548 Z" fill="var(--charcoal)" stroke="var(--gold)" stroke-width="3"/>

      <!-- centre panel showroom circles -->
      <circle cx="530" cy="330" r="98" fill="var(--gold)"/>
      <circle class="photo-mouldings" role="img" aria-label="Stacked lengths of white and natural wood mouldings" cx="530" cy="330" r="90" fill="url(#mouldingTone)"/>
      <circle cx="612" cy="418" r="80" fill="var(--charcoal)"/>
      <circle class="photo-samples" role="img" aria-label="Wall rack of moulding profile samples in the showroom" cx="612" cy="418" r="72" fill="url(#rackTone)"/>

      <!-- front cover: dark header, kitchen image, curves -->
      <rect x="746" y="0" width="374" height="330" fill="var(--charcoal)"/>
      <path d="M746,262 C850,196 1000,172 1120,166 L1120,866 L746,866 Z" fill="var(--paper)"/>
      <path d="M746,250 C850,184 1000,160 1120,152 L1120,166 C1000,172 850,196 746,262 Z" fill="var(--gold)"/>
      <path class="photo-kitchen" role="img" aria-label="White kitchen cabinets with granite counters and wood floor" d="M752,262 C850,204 1000,182 1120,178 L1120,345 C1040,410 900,455 758,470 Z" fill="url(#kitchenTone)"/>
      <path d="M758,470 C900,455 1040,410 1120,345 L1120,372 C1040,440 900,480 758,494 Z" fill="var(--charcoal)"/>
      <path d="M758,484 C900,470 1040,426 1120,362 L1120,380 C1040,448 900,492 760,506 Z" fill="var(--gold)"/>

      <!-- bottom bands -->
      <path d="M0,806 L373,786 L373,826 L0,846 Z" fill="var(--gold)"/>
      <path d="M373,786 L746,766 L746,810 L373,830 Z" fill="var(--charcoal)"/>
      <path d="M746,766 L1120,740 L1120,780 L746,806 Z" fill="var(--gold)"/>

      <!-- fold lines -->
      <line x1="373" y1="0" x2="373" y2="866" stroke="rgba(0,0,0,.08)"/>
      <line x1="746" y1="0" x2="746" y2="866" stroke="rgba(0,0,0,.08)"/>
    </svg>

    <section class="text service-list">
      <h3>Cabinets:</h3>
      <ul>
        <li>Kitchens</li>
        <li>Entertainment Centers</li>
        <li>Vanities</li>
        <li>Mantels</li>
        <li>Bookcases</li>
        <li>Home Offices</li>
      </ul>
      <h3>Mouldings</h3>
      <ul>
        <li>Over 200 Mouldings in Stock</li>
        <li>Free Samples</li>
        <li>Custom Matched Mouldings</li>
        <li>Base, Crown, Casing &amp; many more</li>
        <li>Columns</li>
        <li>Corbels</li>
      </ul>
    </section>
    <p class="text website">www.halvorsenandtate.com</p>

    <section class="text showroom">
      <h2>Come Visit Our Showroom</h2>
      <p>Call : 650-555-0148<br>For a Free Estimate Counter</p>
      <p>318 N. ALDER AVE<br>BELMONT CA 94011</p>
      <p>FAX: 650-555-0149<br>EMAIL: sales@HalvorsenAndTate.com</p>
    </section>

    <header class="text brand">
      <p class="brand-name">Halvorsen &amp; Tate</p>
      <p class="brand-since">SINCE 1943</p>
      <p class="brand-tag">Custom Cabinets &amp; Mouldings</p>
    </header>

    <h1 class="text headline">
      Your place for<br>
      <span class="accent">All wood custom cabinets</span><br>
      And 100's of mouldings<br>
      <span class="accent">All in stock</span>
    </h1>
  </article>
</main>
</body>
</html>
```